Yacht, Boats, Watersports company needs a redesign of business card

Hello Designers!
We are a Boat dealership company that sells fun in the water, we sell boats, Yachts, Kayaks and also yacht WaterSport toys. We are looking to redesign our business cards in to something a little bit more sophisticated. in a way that we can make better use of our company colors. I'm attaching a zipped file containing the company 3 sets of company logo which one is an horizontal another one is a vertical and also a chromed 3d logo. Also is included two set of business cards that we use and also some designs that i think it's interesting. We use PMS 2026c Orange and PMS 7687C Blue. I would like to see at least two different options with the orange as accent and also using blue as an accent color. It's really important for the business cards to have a font option and size that is legible to most people. Our current website is wwww.corvellamarine.com. Please visit if you want to have a better feeling of the Boat dealership
You can send Single sided or double side options. We are now using single sided but we may be open for a double side option if we really like the design.
Target Market(s)
Marine, boat sales, yacht sales, water toys sales/
Contact Information for Business Card
Name: Dale Pritchett
Address: 718 West Halden Lane,
Dania Beach, FL 33019
Phone: 954-382-7146
Fax: 954:382-7139
Cell: 954-451-8320
Email: 212@corvellamarine.com
Website: corvellamarine.com
Requirements
Must have
- the current information of the business card provided.
logo
use the PMS Colors
Nice to have
- a touch of elegance and sophistication but simple
Should not have
- should not have any typography that is hard to read, the card should be simple but yet sophisticated.

```html
<!DOCTYPE html>
<html lang="en">
<head>
<meta charset="utf-8">
<title>Corvella Marine – Business Card</title>
<link href="https://fonts.googleapis.com/css2?family=Montserrat:wght@700;800&family=Questrial&display=swap" rel="stylesheet">
<style>
  :root{
    --backdrop:#5f6164;
    --brand-blue:#154a7d;
    --brand-orange:#f0622f;
    --white:#ffffff;
  }
  *{box-sizing:border-box;margin:0;padding:0}
  html,body{width:1200px;height:1000px;overflow:hidden}
  body{background:var(--backdrop);position:relative;font-family:"Questrial",sans-serif}

  .card{
    position:absolute;width:560px;height:320px;border-radius:26px;
    background:var(--brand-blue);overflow:hidden;
    box-shadow:0 12px 28px rgba(0,0,0,.35);
  }
  .card--front{left:70px;top:110px}
  .card--back{left:570px;top:540px}

  /* front face */
  .front-mark{
    position:absolute;inset:0;display:flex;flex-direction:column;
    align-items:center;justify-content:center;gap:22px;
  }
  .brand-dot{width:96px;height:96px;border-radius:50%;border:12px solid var(--brand-orange)}
  .brand-name{
    font-family:"Montserrat",sans-serif;font-weight:800;color:var(--white);
    letter-spacing:.08em;text-transform:uppercase;
  }
  .front-mark .brand-name{font-size:26px}

  /* back face */
  .back-mark{
    position:absolute;left:30px;top:62px;width:230px;
    display:flex;flex-direction:column;align-items:center;gap:20px;
  }
  .back-mark .brand-dot{width:104px;height:104px;border-width:12px}
  .back-mark .brand-name{font-size:18px}

  .contact{position:absolute;left:286px;top:48px}
  .contact__name{
    font-family:"Montserrat",sans-serif;font-weight:800;font-size:21px;
    color:var(--brand-orange);text-transform:uppercase;margin-bottom:14px;
  }
  .contact__list{list-style:none}
  .contact__item{
    display:flex;align-items:center;gap:10px;height:26px;
    color:var(--white);font-size:15px;letter-spacing:.06em;
  }
  .contact__icon{
    width:19px;height:19px;border-radius:50%;background:var(--brand-orange);
    display:flex;align-items:center;justify-content:center;flex-shrink:0;
  }
  .contact__icon svg{width:11px;height:11px;fill:var(--white)}
  .accent{color:var(--brand-orange)}

  .address-band{
    position:absolute;left:0;right:0;bottom:0;height:70px;
    background:var(--brand-orange);display:flex;align-items:center;padding-left:32px;
    font-family:"Montserrat",sans-serif;font-weight:700;font-size:19px;
    color:var(--white);letter-spacing:.03em;
  }
</style>
</head>
<body>

<section class="card card--front" aria-label="Card front">
  <div class="front-mark">
    <span class="brand-dot" aria-hidden="true"></span>
    <span class="brand-name">Corvella Marine</span>
  </div>
</section>

<section class="card card--back" aria-label="Card back">
  <div class="back-mark">
    <span class="brand-dot" aria-hidden="true"></span>
    <span class="brand-name">Corvella Marine</span>
  </div>

  <div class="contact">
    <h1 class="contact__name">Dale Pritchett</h1>
    <ul class="contact__list">
      <li class="contact__item">
        <span class="contact__icon"><svg viewBox="0 0 24 24"><path d="M6.6 10.8a15 15 0 0 0 6.6 6.6l2.2-2.2a1 1 0 0 1 1-.25 11.4 11.4 0 0 0 3.6.57 1 1 0 0 1 1 1V20a1 1 0 0 1-1 1A17 17 0 0 1 3 4a1 1 0 0 1 1-1h3.5a1 1 0 0 1 1 1c0 1.25.2 2.45.57 3.57a1 1 0 0 1-.25 1z"/></svg></span>
        954-382-7146
      </li>
      <li class="contact__item">
        <span class="contact__icon"><svg viewBox="0 0 24 24"><path d="M7 1h10a2 2 0 0 1 2 2v18a2 2 0 0 1-2 2H7a2 2 0 0 1-2-2V3a2 2 0 0 1 2-2zm0 3v14h10V4zm5 15.5a1 1 0 1 0 0 2 1 1 0 0 0 0-2z"/></svg></span>
        954-451-8320
      </li>
      <li class="contact__item">
        <span class="contact__icon"><svg viewBox="0 0 24 24"><path d="M6 2h10l2 2v5H6zM4 10h16a2 2 0 0 1 2 2v6h-4v4H6v-4H2v-6a2 2 0 0 1 2-2zm4 6v4h8v-4z"/></svg></span>
        954:382-7139
      </li>
      <li class="contact__item">
        <span class="contact__icon"><svg viewBox="0 0 24 24"><path d="M2 5h20v14H2zm2 2v.5l8 5 8-5V7l-8 5z"/></svg></span>
        212@<span class="accent">corvellamarine</span>.com
      </li>
      <li class="contact__item">
        <span class="contact__icon"><svg viewBox="0 0 24 24"><path d="M12 2a10 10 0 1 0 0 20 10 10 0 0 0 0-20zm0 2c.9 1.2 1.6 2.8 1.9 5h-3.8c.3-2.2 1-3.8 1.9-5zM4.3 13h3.8c.1 1.9.5 3.6 1.1 4.9A8 8 0 0 1 4.3 13zm0-2a8 8 0 0 1 4.9-4.9C8.6 7.4 8.2 9.1 8.1 11zm5.8 2h3.8c-.3 2.2-1 3.8-1.9 5-.9-1.2-1.6-2.8-1.9-5zm5.8 0h3.8a8 8 0 0 1-4.9 4.9c.6-1.3 1-3 1.1-4.9zm0-2c-.1-1.9-.5-3.6-1.1-4.9A8 8 0 0 1 19.7 11z"/></svg></span>
        www.<span class="accent">corvellamarine</span>.com
      </li>
    </ul>
  </div>

  <div class="address-band">718 West Halden Lane, Dania Beach, FL 33019</div>
</section>

</body>
</html>
```